Nolvik Imaging Center web design and code

We need a new website for a Diagnostic Imaging Center in Fort Lauderdale, Florida.
The center has new RO advanced diagnostic equipment including a 3.0 Tesla MRI, a 128 slice PET/CT and a Varen T4 Ultrasound. Our facility has just been renovated and we have a lot of images, both facility and modality to use.
We have two client types, doctors who send their patients to our clinical Nolvik Center division, and clients who self-refer for screening studies to our Wellspire division. Both logos are attached. Please use the colors in the logos for the layout. Site should be coded in conventional HTML with CSS, but support multiple devices.
Updates

Reason: Waiting for additional designs. Most of the current designs are very similar in their structure and we would like more variety in terms of layout.

Target Market(s)

Doctors who refer patients for MRI, CT, PET, Bone Density and Ultrasound scans,
and
Retail clients who want full-body screening using MRI.

Industry/Entity Type

Medical Imaging

Coding

Coded - Design and coding required

Number of Pages Required

5+ page

Font styles to use
Sans Serif
Other font styles liked:
• Arquitecta

Requirements
Must have
• A good balance between color, shape, message and people/machine images.
• Must have images of the various machines, (RO Quillmark TN480, RO Quillmark 370, RO Varen T4) happy patients, clinical people, facility images and information about scans, preparations, costs, insurances we take.
• Must have links for social media and dynamic imagery.
Nice to have
• Some interactivity would be nice, including contact forms and scheduling application, Location map, directions, downloadable forms, history.
Should not have
• We do not want this to be built on WordPress platform. Should not be bound to a database platform that is proprietary or difficult to move.

```html
<!DOCTYPE html>
<html lang="en">
<head>
<meta charset="utf-8">
<title>Nolvik Imaging Center</title>
<link href="https://fonts.googleapis.com/css2?family=Raleway:wght@400;600;700;800&family=Open+Sans:wght@400;600;700&display=swap" rel="stylesheet">
<style>
:root{
  --green:#8dc63f;
  --green-dark:#76ab2c;
  --ink:#3a3f44;
  --text:#6f767c;
  --muted:#9aa1a7;
  --topbar:#2e3236;
  --form-band:#3d4247;
  --news-bg:#f2f3f4;
  --quote-bg:#3b4650;
  --footer:#30353a;
  --footer-base:#272b2f;
  --white:#ffffff;
  --line:#e3e6e8;
}
*{box-sizing:border-box;margin:0;padding:0}
html,body{width:1200px;height:3520px;overflow:hidden}
body{font-family:'Open Sans',Arial,sans-serif;color:var(--text);background:var(--white);position:relative;font-size:13px;line-height:1.6}
h1,h2,h3,h4,.display{font-family:'Raleway',Arial,sans-serif;color:var(--ink)}
.section{position:absolute;left:0;width:1200px}
.wrap{position:absolute;left:100px;width:1000px}
.btn{display:inline-block;background:var(--green);color:var(--white);font-family:'Raleway',Arial,sans-serif;font-weight:700;font-size:12px;letter-spacing:.5px;padding:10px 22px;border-radius:2px;text-transform:uppercase}
.btn-dark{background:var(--ink)}
.photo{display:block}

/* top bar */
.topbar{top:0;height:32px;background:var(--topbar);color:#c9ced2;font-size:11px}
.topbar .wrap{top:0;height:32px;display:flex;justify-content:space-between;align-items:center}
.topbar b{color:var(--green);font-weight:700;margin-right:6px}

/* header */
.header{top:32px;height:128px;background:var(--white);border-bottom:1px solid var(--line)}
.brand{position:absolute;left:100px;top:34px;display:flex;align-items:center;gap:14px}
.brand-dot{width:58px;height:58px;border-radius:50%;background:var(--green)}
.brand-name{font-family:'Raleway',Arial,sans-serif;font-weight:700;font-size:26px;line-height:1.1;color:var(--ink);text-transform:uppercase}
.nav{position:absolute;right:100px;top:52px;display:flex;gap:30px;font-family:'Raleway',Arial,sans-serif;font-weight:700;font-size:12px;color:var(--ink);letter-spacing:.5px}
.nav .active{color:var(--green)}

/* hero */
.hero{top:160px;height:430px}
.hero .photo{position:absolute;inset:0;background:linear-gradient(100deg,#9fb3bd 0%,#d7e1e6 35%,#eef2f4 60%,#c6d3da 100%)}
.hero-card{position:absolute;left:100px;top:128px;width:520px}
.hero-card h1{background:var(--green);color:var(--white);font-weight:800;font-size:36px;line-height:1.15;padding:14px 20px;text-transform:uppercase}
.hero-card h1 span{color:#eaf6d6}
.hero-card p{background:rgba(58,63,68,.85);color:var(--white);font-size:12px;padding:12px 20px;text-transform:uppercase;letter-spacing:.3px}
.hero-card .btn{margin-top:14px;font-size:11px;padding:8px 18px}
.dots{position:absolute;left:568px;top:388px;display:flex;gap:8px}
.dots i{width:10px;height:10px;border-radius:50%;background:rgba(255,255,255,.6)}
.dots i:first-child{background:var(--white)}

/* appointment */
.appoint{top:590px;height:122px;background:var(--form-band)}
.appoint-tab{position:absolute;left:100px;top:0;background:var(--green);color:var(--white);font-family:'Raleway',Arial,sans-serif;font-weight:700;font-size:13px;padding:8px 18px}
.field{position:absolute;height:30px;border:1px solid var(--green);background:var(--green);color:var(--white);font-size:11px;font-weight:600;padding:6px 12px}
.appoint .send{position:absolute;left:1036px;top:78px;width:64px;height:30px;background:var(--white);color:var(--ink);font-family:'Raleway',Arial,sans-serif;font-weight:800;font-size:12px;text-align:center;line-height:30px}

/* services */
.services{top:712px;height:420px}
.intro{position:absolute;left:100px;top:58px;width:290px}
.intro h2{font-weight:700;font-size:26px;line-height:1.15;text-transform:uppercase;margin-bottom:16px}
.intro h2 span{color:var(--green)}
.intro p{font-size:12px;margin-bottom:26px}
.service{position:absolute;width:320px;display:flex;gap:18px}
.service-icon{flex:none;width:52px;height:52px;background:var(--green);border-radius:4px;display:flex;align-items:center;justify-content:center}
.service h3{font-size:18px;font-weight:600;margin-bottom:6px}
.service p{font-size:12px}

/* news */
.news{top:1132px;height:770px;background:var(--news-bg)}
.heading{position:absolute;left:0;width:1200px;text-align:center}
.heading h2{font-size:24px;font-weight:700;text-transform:uppercase}
.heading p{font-size:11px;color:var(--muted);margin-top:6px}
.rule{width:46px;height:3px;background:var(--green);margin:12px auto 0}
.feature{position:absolute;left:100px;top:150px;width:490px;height:490px;background:var(--white)}
.feature .photo{position:absolute;left:0;top:0;width:490px;height:300px;background:linear-gradient(135deg,#dfe7ec,#b9c9d3)}
.date{position:absolute;left:0;top:0;background:var(--green);color:var(--white);font-family:'Raleway',Arial,sans-serif;font-weight:700;font-size:12px;padding:8px 16px}
.feature-body{position:absolute;left:24px;top:318px;width:440px}
.feature-body h3{font-size:15px;font-weight:700;margin-bottom:8px}
.feature-body p{font-size:12px}
.more{display:block;margin-top:12px;color:var(--green);font-size:11px;font-weight:700}
.mini{position:absolute;width:235px;height:235px;background:var(--white)}
.mini .photo{width:235px;height:150px;background:linear-gradient(135deg,#e4ecf0,#c2d2db)}
.mini p{font-size:12px;color:var(--ink);padding:12px 14px;line-height:1.5}
.news .btn{position:absolute;left:515px;top:700px;width:170px;text-align:center}

/* testimonials */
.quotes{top:1902px;height:458px;background:var(--quote-bg);color:#c5ccd2}
.quotes .heading h2{color:var(--white)}
.quotes .heading p{color:#aab3ba}
.quote-text{position:absolute;left:180px;top:210px;width:840px;text-align:center;font-size:15px;line-height:1.8;color:#dfe4e8}
.author{position:absolute;left:0;width:1200px;top:300px;display:flex;justify-content:center;align-items:center;gap:12px;font-size:11px}
.avatar{width:44px;height:44px;border-radius:50%;background:linear-gradient(135deg,#c9b8a6,#8e7b6c)}
.author b{color:var(--white);font-family:'Raleway',Arial,sans-serif}
.arrow{position:absolute;top:232px}

/* specialists */
.team{top:2360px;height:740px}
.team .heading h2{text-transform:none;font-weight:400;font-size:28px}
.team .heading h2 span{color:var(--green);font-weight:600}
.doctor{position:absolute;top:150px;width:232px;height:520px;background:var(--white);border:1px solid var(--line);text-align:center}
.doctor .photo{width:230px;height:220px;background:linear-gradient(180deg,#e9eff2,#c7d6de)}
.doctor h3{font-size:16px;font-weight:600;margin-top:22px}
.doctor .bar{width:36px;height:2px;background:var(--green);margin:12px auto}
.doctor p{font-size:12px;padding:0 18px;line-height:1.65}
.doctor .btn{margin-top:18px;font-size:11px;padding:8px 18px;text-transform:none}

/* footer */
.footer{top:3100px;height:380px;background:var(--footer);color:#a7aeb4;font-size:12px}
.col{position:absolute;top:60px;width:220px}
.col h4{color:var(--white);font-size:15px;font-weight:700;margin-bottom:18px}
.col li{list-style:none;padding:7px 0;border-bottom:1px solid #3e444a}
.col p{margin-bottom:14px}
.input{height:32px;background:#3d4349;margin:6px 0 14px}
.label{color:#c7cdd2}
.socials{position:absolute;right:100px;top:18px;display:flex;gap:10px}
.socials i{width:24px;height:24px;border-radius:50%;background:#454b51}
.base{top:3480px;height:40px;background:var(--footer-base);color:#8a9197;font-size:11px}
.base .wrap{top:0;height:40px;display:flex;align-items:center}
</style>
</head>
<body>

<div class="section topbar">
  <div class="wrap">
    <span><b>OPENING HOURS:</b>Monday to Saturday - 8am to 7pm</span>
    <span><b>CONTACT:</b>+1 (555) 014-2290</span>
  </div>
</div>

<header class="section header">
  <div class="brand">
    <div class="brand-dot"></div>
    <div class="brand-name">Nolvik<br>Imaging Center</div>
  </div>
  <nav class="nav">
    <span class="active">HOME</span><span>DOCTORS</span><span>SERVICES</span><span>PAGES</span><span>NEWS</span><span>ELEMENTS</span><span>CONTACT</span>
  </nav>
</header>

<section class="section hero">
  <div class="photo" role="img" aria-label="Patient lying on an MRI scanner table with a technician in a bright scan room"></div>
  <div class="hero-card">
    <h1>Providing total <span>health</span><br>care solution</h1>
    <p>Forth fruit beginning life, likeness dry day from him<br>rule it earth unto seas fourth.</p>
    <span class="btn">Read more</span>
  </div>
  <div class="dots"><i></i><i></i><i></i></div>
</section>

<section class="section appoint">
  <div class="appoint-tab">Make an Appointment</div>
  <div class="field" style="left:100px;top:40px;width:235px">Name</div>
  <div class="field" style="left:355px;top:40px;width:235px">Phone Number</div>
  <div class="field" style="left:610px;top:40px;width:235px">Email Address</div>
  <div class="field" style="left:865px;top:40px;width:235px">Appointment Date</div>
  <div class="field" style="left:100px;top:78px;width:916px">Message</div>
  <div class="send">SEND</div>
</section>

<section class="section services">
  <div class="intro">
    <h2>Nolvik Scan &amp;<br><span>Imaging</span> Center</h2>
    <p>Lorem ipsum dolor sit amet, consectetur adipiscing elit. Sed diam nonummy nibh euismod tincidunt ut laoreet dolore magna aliquam erat volutpat.</p>
    <span class="btn btn-dark">View our services</span>
  </div>
  <div class="service" style="left:460px;top:56px">
    <div class="service-icon"><svg width="26" height="26" viewBox="0 0 26 26"><path d="M10 2h6v8h8v6h-8v8h-6v-8H2v-6h8z" fill="#fff"/></svg></div>
    <div><h3>Rehabilitation Center</h3><p>Lorem ipsum dolor sit amet, consectetur adipiscing elit sed diam nonummy nibh euismod tincidunt.</p></div>
  </div>
  <div class="service" style="left:780px;top:56px">
    <div class="service-icon"><svg width="26" height="26" viewBox="0 0 26 26"><rect x="3" y="7" width="20" height="15" rx="2" fill="#fff"/><rect x="9" y="3" width="8" height="5" fill="none" stroke="#fff" stroke-width="2"/><path d="M11.5 10h3v3h3v3h-3v3h-3v-3h-3v-3h3z" fill="#8dc63f"/></svg></div>
    <div><h3>Medical Counseling</h3><p>Lorem ipsum dolor sit amet, consectetur adipiscing elit sed diam nonummy nibh euismod tincidunt.</p></div>
  </div>
  <div class="service" style="left:460px;top:196px">
    <div class="service-icon"><svg width="26" height="26" viewBox="0 0 26 26"><circle cx="13" cy="8" r="5" fill="#fff"/><path d="M3 24c0-6 4.5-9 10-9s10 3 10 9z" fill="#fff"/></svg></div>
    <div><h3>Qualified Doctors</h3><p>Lorem ipsum dolor sit amet, consectetur adipiscing elit sed diam nonummy nibh euismod tincidunt.</p></div>
  </div>
  <div class="service" style="left:780px;top:196px">
    <div class="service-icon"><svg width="26" height="26" viewBox="0 0 26 26"><rect x="2" y="8" width="16" height="11" fill="#fff"/><path d="M18 11h4l3 4v4h-7z" fill="#fff"/><circle cx="7" cy="21" r="2.5" fill="#fff"/><circle cx="20" cy="21" r="2.5" fill="#fff"/><path d="M9 10h2v2h2v2h-2v2H9v-2H7v-2h2z" fill="#8dc63f"/></svg></div>
    <div><h3>Emergency Services</h3><p>Lorem ipsum dolor sit amet, consectetur adipiscing elit sed diam nonummy nibh euismod tincidunt.</p></div>
  </div>
</section>

<section class="section news">
  <div class="heading" style="top:62px">
    <h2>Latest News &amp; Events</h2>
    <p>Stay updated with our latest news and upcoming events</p>
    <div class="rule"></div>
  </div>
  <article class="feature">
    <div class="photo" role="img" aria-label="Smiling doctor in a white coat holding a clipboard"></div>
    <div class="date">MAY 11, 2015</div>
    <div class="feature-body">
      <h3>New crisp hope invades of regaining tumor cells</h3>
      <p>Lorem ipsum dolor sit amet, consectetur adipiscing elit. Aenean commodo ligula eget dolor massa cum sociis natoque penatibus et magnis dis parturient.</p>
      <span class="more">+ Read More</span>
    </div>
  </article>
  <article class="mini" style="left:610px;top:150px">
    <div class="photo" role="img" aria-label="Doctor reviewing patient notes"></div>
    <p>New blood test can quickly diagnose irritable bowel syndrome.</p>
  </article>
  <article class="mini" style="left:865px;top:150px">
    <div class="photo" role="img" aria-label="Modern clinic building exterior"></div>
    <p>Family history may not advance effect on breast cancer outcomes.</p>
  </article>
  <article class="mini" style="left:610px;top:405px">
    <div class="photo" role="img" aria-label="Team of medical staff in a corridor"></div>
    <p>Brain area that calculates quickest timing discovered.</p>
  </article>
  <article class="mini" style="left:865px;top:405px">
    <div class="photo" role="img" aria-label="Nurse talking with an older patient"></div>
    <p>Metabolic syndrome affects more than a third of Americans.</p>
  </article>
  <span class="btn">View all our news</span>
</section>

<section class="section quotes">
  <svg class="arrow" style="left:100px" width="16" height="26" viewBox="0 0 16 26"><path d="M13 3L4 13l9 10" fill="none" stroke="#fff" stroke-width="3"/></svg>
  <svg class="arrow" style="right:100px" width="16" height="26" viewBox="0 0 16 26"><path d="M3 3l9 10-9 10" fill="none" stroke="#fff" stroke-width="3"/></svg>
  <div class="heading" style="top:60px">
    <svg width="34" height="26" viewBox="0 0 34 26"><path d="M0 26V14C0 6 4 1 12 0v5c-4 1-6 4-6 8h6v13zM20 26V14c0-8 4-13 12-14v5c-4 1-6 4-6 8h6v13z" fill="#8dc63f"/></svg>
    <h2 style="margin-top:14px">What our patients have to say</h2>
    <p>Real experiences from our patients</p>
  </div>
  <p class="quote-text">Second dominion saying one void beast. Called appear multiply light that. Whose after fish likeness meat bring one night fill for gathering day let together set second cloth fish them place thing green beast isn't isn't tree.</p>
  <div class="author">
    <div class="avatar" role="img" aria-label="Patient portrait"></div>
    <span><b>LENA ORVIK</b> / Patient since 2013</span>
  </div>
</section>

<section class="section team">
  <div class="heading" style="top:70px">
    <h2>Meet our <span>Medical Specialists</span></h2>
    <p>Lorem ipsum dolor sit amet, consectetur adipiscing elit, sed diam nonummy nibh euismod tincidunt ut laoreet dolore magna aliquam erat volutpat.</p>
  </div>
  <div class="doctor" style="left:100px">
    <div class="photo" role="img" aria-label="Portrait of a male doctor with stethoscope"></div>
    <h3>Dr. Hollis Arvane</h3><div class="bar"></div>
    <p>The most experienced, trusted imaging specialist on our team, caring for patients with skill and attention every day.</p>
    <span class="btn">Read More</span>
  </div>
  <div class="doctor" style="left:356px">
    <div class="photo" role="img" aria-label="Portrait of a female doctor in scrubs"></div>
    <h3>Dr. Mirel Castow</h3><div class="bar"></div>
    <p>The most experienced, trusted imaging specialist on our team, caring for patients with skill and attention every day.</p>
    <span class="btn">Read More</span>
  </div>
  <div class="doctor" style="left:612px">
    <div class="photo" role="img" aria-label="Portrait of a male doctor in a white coat"></div>
    <h3>Dr. Teodor Vaske</h3><div class="bar"></div>
    <p>The most experienced, trusted imaging specialist on our team, caring for patients with skill and attention every day.</p>
    <span class="btn">Read More</span>
  </div>
  <div class="doctor" style="left:868px">
    <div class="photo" role="img" aria-label="Portrait of a female surgeon in a cap"></div>
    <h3>Dr. Ilsa Pendrow</h3><div class="bar"></div>
    <p>The most experienced, trusted imaging specialist on our team, caring for patients with skill and attention every day.</p>
    <span class="btn">Read More</span>
  </div>
</section>

<footer class="section footer">
  <div class="col" style="left:100px">
    <h4>About Nolvik</h4>
    <p>Lorem ipsum dolor sit amet, consectetur adipiscing elit, sed diam nonummy nibh euismod tincidunt ut laoreet dolore magna.</p>
    <p>Ut wisi enim ad minim veniam, quis nostrud exerci tation ullamcorper suscipit lobortis nisl ut aliquip.</p>
  </div>
  <div class="col" style="left:360px">
    <h4>Latest Tweets</h4>
    <p>New scan hours now open on Saturdays for all imaging studies. <span style="color:var(--green)">#nolvik</span><br>2 days ago</p>
    <p>Read our guide to preparing for your first MRI appointment. <span style="color:var(--green)">#health</span><br>5 days ago</p>
  </div>
  <div class="col" style="left:620px">
    <h4>Recent Posts</h4>
    <ul>
      <li>Image Post Format</li>
      <li>Quote Post Format</li>
      <li>Gallery Post Format</li>
      <li>How to Prepare for a Scan</li>
      <li>This Year in Review</li>
    </ul>
  </div>
  <div class="col" style="left:880px">
    <h4>Newsletter Sign Up</h4>
    <p>Get updates and health tips from our imaging team.</p>
    <div class="label">Name</div><div class="input"></div>
    <div class="label">Email</div><div class="input"></div>
    <span class="btn">Submit</span>
  </div>
</footer>

<div class="section base">
  <div class="wrap">© Copyright 2015. Nolvik Imaging Center. All rights reserved.</div>
  <div class="socials"><i></i><i></i><i></i><i></i><i></i></div>
</div>

</body>
</html>
```